Banner design

I need four banners for my website, www.KursVindu.nu. I am not a designer, as you can see – I teach Brindle Suite, but I need my site to be good looking at get some customers.

See atachede PDF file for more information

Industry/Entity Type

Office

```html
<!DOCTYPE html>
<html lang="en">
<head>
<meta charset="utf-8">
<title>KursVindu.nu – Banner Set</title>
<link rel="stylesheet" href="https://fonts.googleapis.com/css2?family=Arimo:wght@400;700&display=swap">
<style>
  :root {
    --page: #ffffff;
    --ink: #222222;
    --caption: #333333;
    --orange: #e2411c;
    --orange-dark: #c9330f;
    --blue: #39a3d6;
    --crimson: #b8232d;
    --crimson-light: #c72a35;
    --green: #6aa83a;
    --green-light: #79b846;
    --badge-light: #f1f1f1;
    --badge-dark: #111111;
    --white: #ffffff;
  }
  * { box-sizing: border-box; margin: 0; padding: 0; }
  html, body {
    width: 1200px; height: 1137px; overflow: hidden;
    background: var(--page);
    font-family: "Arimo", Arial, sans-serif;
  }
  .sheet { position: relative; width: 1200px; height: 1137px; }

  .banner {
    position: absolute; left: 47px; width: 1097px; height: 139px;
    border: 2px solid var(--accent);
    border-bottom: 11px solid var(--accent);
    background: var(--white);
    overflow: hidden;
  }
  .banner--start { top: 91px; --accent: var(--orange); }
  .banner--software { top: 305px; --accent: var(--blue); }
  .banner--subscribe { top: 600px; --accent: var(--crimson); }
  .banner--slogan { top: 867px; --accent: var(--green); }

  .brand {
    position: absolute; left: 92px; top: 22px;
    display: flex; align-items: center; gap: 14px;
  }
  .brand__name {
    font-weight: 700; font-size: 34px; line-height: 38px;
    color: var(--ink); letter-spacing: -0.5px;
  }
  .brand__mark { width: 30px; height: 30px; background: var(--orange); }

  .start-block {
    position: absolute; left: 387px; top: 0; width: 340px; height: 100%;
    background: linear-gradient(180deg, var(--orange) 0%, var(--orange-dark) 100%);
    border-left: 4px solid #f0a48f; border-right: 4px solid #f0a48f;
    display: flex; align-items: center; justify-content: center;
    color: var(--white); font-weight: 700; font-size: 36px;
  }
  .cert-badge {
    position: absolute; left: 834px; top: 17px; width: 157px; height: 96px;
    border: 2px solid #888; border-radius: 4px; background: var(--badge-light);
    overflow: hidden;
  }
  .cert-badge::after {
    content: ""; position: absolute; left: 0; right: 0; bottom: 0; height: 26px;
    background: var(--badge-dark);
  }

  .product {
    position: absolute; left: 472px; top: 22px;
    display: flex; align-items: center; gap: 38px;
  }
  .product__icon { width: 78px; height: 78px; }
  .product__name { font-weight: 700; font-size: 32px; color: var(--ink); }

  .subscribe-block {
    position: absolute; left: 382px; top: 4px; width: 626px; bottom: 0;
    background: linear-gradient(180deg, var(--crimson-light) 0%, var(--crimson) 100%);
    display: flex; align-items: center; justify-content: center;
    color: var(--white); font-weight: 700; font-size: 32px;
  }

  .slogan-shape { position: absolute; left: 0; top: 0; width: 1093px; height: 126px; }
  .slogan-text {
    position: absolute; left: 457px; width: 600px; top: 0; height: 126px;
    display: flex; align-items: center; justify-content: center;
    color: var(--white); font-weight: 700; font-size: 32px;
  }

  .caption {
    position: absolute; left: 47px; width: 1120px;
    font-size: 27px; line-height: 36px; color: var(--caption);
  }
  .caption--start { top: 232px; }
  .caption--software { top: 452px; }
  .caption--subscribe { top: 747px; }
  .caption--slogan { top: 1013px; }
</style>
</head>
<body>
<main class="sheet">

  <section class="banner banner--start">
    <div class="brand"><span class="brand__name">Kurs<br>Vindu.nu</span><span class="brand__mark"></span></div>
    <div class="start-block">Start</div>
    <div class="cert-badge" role="img" aria-label="Certification badge"></div>
  </section>
  <p class="caption caption--start">Banner 1</p>

  <section class="banner banner--software">
    <div class="brand"><span class="brand__name">Kurs<br>Vindu.nu</span><span class="brand__mark"></span></div>
    <div class="product">
      <svg class="product__icon" viewBox="0 0 78 78" aria-hidden="true">
        <rect x="0" y="0" width="78" height="78" rx="6" fill="#4a8fd8"/>
        <rect x="16" y="16" width="46" height="46" fill="none" stroke="#ffffff" stroke-width="5"/>
      </svg>
      <span class="product__name">Brindle Project</span>
    </div>
  </section>
  <p class="caption caption--software">Banner 2 - Designed to animate and switch between software names. Its not currently animated but the layers are all there. If you need me to animate it I can.</p>

  <section class="banner banner--subscribe">
    <div class="brand"><span class="brand__name">Kurs<br>Vindu.nu</span><span class="brand__mark"></span></div>
    <div class="subscribe-block">Subscribe to Tip of the Week</div>
  </section>
  <p class="caption caption--subscribe">Banner 3 - Obviously its in English but if you give me the Dutch translation I would be happy to revise it for you.</p>

  <section class="banner banner--slogan">
    <div class="brand"><span class="brand__name">Kurs<br>Vindu.nu</span><span class="brand__mark"></span></div>
    <svg class="slogan-shape" viewBox="0 0 1093 126" aria-hidden="true">
      <defs>
        <linearGradient id="slogan-fill" x1="0" y1="0" x2="0" y2="1">
          <stop offset="0" stop-color="#79b846"/>
          <stop offset="1" stop-color="#6aa83a"/>
        </linearGradient>
      </defs>
      <path d="M338 126 C 380 70, 410 20, 470 0 L 1053 0 C 1020 40, 990 90, 972 126 Z" fill="url(#slogan-fill)"/>
    </svg>
    <div class="slogan-text">Insert Slogan Here</div>
  </section>
  <p class="caption caption--slogan">Banner 4 - Again, I dont speak Dutch but if you have any slogans you'd like in the banner please let me know.</p>

</main>
</body>
</html>
```